Organic CBD topicals needs product labels for body butters, roll on oils and massage oil candles

We are looking for product labels that fit our growing brand, We are yogi's making organic CBD infused topicals that help people with pain relief and healing through plant based creams and oils, naturally, without side effects. We have body butter balms that come in 2oz tins, we have massage oil candles in 6oz, mandala design tins with a lid, we have infused essential oils in frosted glass bottles with healing gemstone roller balls, we also make lip balms in both 1/2 oz tins and lip balm sticks, as well as a 2oz twist up body butter balm. I would like the labels to have a yogi/chakra feel to them. The body butter balms come in different strengths, so it would be great if the strongest 600mg start at the base chakra, using the chakre color scale and go up from there. 300mg, 150mg then pure CBD, then up the chakra scale for the other products, 1:1, 3:1 and 30:1 for the roll on essential oils and massage oil candles.

You can see our products here: www.lunavalebotanics.org

Kivo Body Butter Balm label 2 1/2" round.
Matching 2" label for the bottom of the tin with ingredients & instructions.
Massage Oil Candle label 1 1/2 round
Bottom of Candle label 2" round for ingredients & instructions
Spiraled Kivo Body Butter Label 4 1'2 wide x 2 1/2 tall Square
Twist up lip balm label can be 2 1/4 w x 1 1/2 tall
Lip Balm tin label 1" round

Target Market(s)

Everyone that has pain, injuries, headaches, skin conditions, etc... and wants to deal with them naturally, without big pharma and their terrible medicines that come with killer side effects.

Font styles to use
Serif
Sans Serif

Requirements
Must have
• A yogi look and feel, chakra colors, symbols and our logo featured prominently
Should not have
• a corporate look or feel

```html
<!DOCTYPE html>
<html lang="en">
<head>
<meta charset="utf-8">
<title>Kivo Organic – Body Butter Salve Labels</title>
<link href="https://fonts.googleapis.com/css2?family=Almendra:wght@700&family=Alegreya:wght@400;500&family=Crimson+Text:wght@400&display=swap" rel="stylesheet">
<style>
  :root {
    --sky: #a9dbe8;
    --sky-soft: #c4e5ee;
    --brown: #5a1e0c;
    --brown-band: #5b1a0b;
    --cream: #fbe7a8;
    --cream-edge: #f5d98a;
    --orange: #f2a85a;
    --peach: #f6c27a;
    --lime: #b6d86a;
    --green: #9fd36a;
    --mandala-red: #c8452a;
    --mandala-orange: #e0712f;
    --mandala-yellow: #e9c25a;
    --mandala-green: #93b26c;
    --mandala-teal: #74c4c6;
    --mandala-indigo: #7c86c8;
    --mandala-violet: #b98ad2;
    --ink: #4a1a10;
    --white: #ffffff;
    --page: #ffffff;
  }
  * { box-sizing: border-box; margin: 0; padding: 0; }
  html, body { width: 1200px; height: 1200px; overflow: hidden; background: var(--page); }
  .canvas { position: relative; width: 1200px; height: 1200px; }

  /* ---------- Front lid label ---------- */
  .label-front {
    position: absolute; left: 50px; top: 330px;
    width: 540px; height: 540px; border-radius: 50%;
    background: radial-gradient(circle, var(--peach) 0%, var(--cream-edge) 55%, var(--sky-soft) 78%, var(--sky) 100%);
  }
  .mandala-field {
    position: absolute; left: 58px; top: 48px; width: 424px; height: 424px; border-radius: 50%;
    background:
      radial-gradient(circle, rgba(0,0,0,0) 0%, rgba(0,0,0,0) 97%, rgba(255,255,255,0) 100%),
      radial-gradient(circle,
        var(--cream) 0%,
        var(--mandala-violet) 24%,
        var(--mandala-indigo) 31%,
        var(--mandala-green) 40%,
        var(--mandala-yellow) 48%,
        var(--mandala-orange) 56%,
        var(--mandala-teal) 66%,
        var(--mandala-green) 75%,
        var(--mandala-orange) 86%,
        var(--mandala-red) 93%,
        rgba(224,113,47,0) 100%);
  }
  .front-title {
    position: absolute; left: 0; right: 0; top: 78px; text-align: center;
    font-family: "Almendra", serif; font-weight: 700; font-size: 52px; color: var(--brown);
    -webkit-text-stroke: 1.5px var(--cream); paint-order: stroke fill;
  }
  .front-sub {
    position: absolute; left: 0; right: 0; top: 146px; text-align: center;
    font-family: "Alegreya", serif; font-size: 27px; color: var(--brown);
  }
  .brand-disc {
    position: absolute; left: 195px; top: 192px; width: 150px; height: 150px; border-radius: 50%;
    background: var(--cream); display: flex; align-items: center; justify-content: center; text-align: center;
  }
  .brand-name {
    font-family: "Crimson Text", serif; font-size: 19px; color: var(--brown); letter-spacing: 1px; line-height: 1.15;
  }
  .cbd-band {
    position: absolute; left: 140px; top: 360px; width: 260px; height: 34px; background: var(--brown-band);
    display: flex; align-items: center; justify-content: center;
    font-family: "Almendra", serif; font-weight: 700; font-size: 21px; color: var(--cream);
  }
  .front-scent {
    position: absolute; left: 0; right: 0; top: 400px; text-align: center;
    font-family: "Alegreya", serif; font-size: 18px; line-height: 1.3; color: var(--brown);
  }
  .net-weight {
    position: absolute; left: 0; right: 0; text-align: center;
    font-family: "Crimson Text", serif; color: var(--ink);
  }
  .label-front .net-weight { top: 488px; font-size: 13px; }

  /* ---------- Bottom tin label ---------- */
  .label-back {
    position: absolute; left: 660px; top: 380px;
    width: 440px; height: 440px; border-radius: 50%;
    background: radial-gradient(circle at 50% 48%,
      var(--green) 0%, var(--lime) 20%, var(--cream-edge) 36%,
      var(--peach) 50%, var(--orange) 64%, var(--peach) 74%,
      var(--sky-soft) 88%, var(--sky) 100%);
  }
  .back-disc {
    position: absolute; left: 170px; top: 22px; width: 100px; height: 100px; border-radius: 50%;
    background: var(--cream); display: flex; align-items: center; justify-content: center; text-align: center;
  }
  .back-disc .brand-name { font-size: 13px; }
  .back-title {
    position: absolute; left: 0; right: 0; top: 132px; text-align: center;
    font-family: "Almendra", serif; font-weight: 700; font-size: 30px; color: var(--brown);
  }
  .back-sub {
    position: absolute; left: 0; right: 0; top: 172px; text-align: center;
    font-family: "Alegreya", serif; font-size: 17px; color: var(--brown);
  }
  .divider { position: absolute; left: 170px; top: 202px; width: 100px; height: 8px; }
  .back-copy {
    position: absolute; left: 40px; right: 40px; top: 214px; text-align: justify; text-align-last: center;
    font-family: "Crimson Text", serif; font-size: 11.5px; line-height: 1.02; color: var(--ink);
  }
  .back-ingredients {
    position: absolute; left: 0; right: 0; top: 272px; text-align: center;
    font-family: "Alegreya", serif; font-size: 17px; line-height: 1.05; color: var(--brown);
  }
  .batch-box { position: absolute; left: 140px; top: 318px; width: 160px; height: 48px; background: var(--white); }
  .back-url {
    position: absolute; left: 0; right: 0; top: 374px; text-align: center;
    font-family: "Crimson Text", serif; font-size: 11px; color: var(--ink);
  }
  .label-back .net-weight { top: 398px; font-size: 12px; }
</style>
</head>
<body>
<main class="canvas">

  <section class="label-front" aria-label="Front lid label">
    <div class="mandala-field" role="img" aria-label="Chakra-coloured mandala ornament ring in violet, indigo, green, yellow, orange, teal and red"></div>
    <h1 class="front-title">Kivo Organic</h1>
    <p class="front-sub">~Body Butter Salve~</p>
    <div class="brand-disc"><span class="brand-name">LUNAVALE<br>BOTANICS</span></div>
    <div class="cbd-band">Contains Pure CBD</div>
    <p class="front-scent">Eucalyptus, Cedar<br>&amp; Chamomile</p>
    <p class="net-weight">Net NT. 2 oz.</p>
  </section>

  <section class="label-back" aria-label="Bottom tin label">
    <div class="back-disc"><span class="brand-name">LUNAVALE<br>BOTANICS</span></div>
    <h2 class="back-title">Kivo Organic</h2>
    <p class="back-sub">~Body Butter Salve~</p>
    <svg class="divider" viewBox="0 0 100 8" aria-hidden="true">
      <line x1="0" y1="4" x2="38" y2="4" stroke="#3f6fb0" stroke-width="1"/>
      <circle cx="44" cy="4" r="2" fill="#3f6fb0"/>
      <circle cx="50" cy="4" r="2" fill="#3f6fb0"/>
      <circle cx="56" cy="4" r="2" fill="#3f6fb0"/>
      <line x1="62" y1="4" x2="100" y2="4" stroke="#3f6fb0" stroke-width="1"/>
    </svg>
    <p class="back-copy">Sed ut perspiciatis unde omnis iste natus error sit voluptatem accusantium doloremque laudantium, totam rem aperiam, eaque ipsa quae ab illo inventore veritatis et quasi architecto beatae Sed ut perspiciatis unde omnis iste natus</p>
    <p class="back-ingredients">Ingredients : Eucalyptus,<br>Cedar &amp; Chamomile</p>
    <div class="batch-box"></div>
    <p class="back-url">www.lunavalebotanics.org</p>
    <p class="net-weight">Net NT. 2 oz.</p>
  </section>

</main>
</body>
</html>
```